Trulock Property Inspections

Property Inspection ( pre-purchase building inspections, swimming pool inspection, pest inspection , maintenance)

Industry/Entity Type

Building

Contact Information for Business Card

Omar Tanvelli
info@trulockinspections.com.au
0417 828 691

TruLock Property Inspections
www.trulockinspections.com.au

on the back

Property Inspections
Property Maintenance

Safe Home....Safe Familu

```html
<!DOCTYPE html>
<html lang="en">
<head>
<meta charset="utf-8">
<title>TruLock Property Inspections – Business Card</title>
<link rel="stylesheet" href="https://fonts.googleapis.com/css2?family=Titillium+Web:wght@400;600;700&family=Courgette&display=swap">
<style>
  :root {
    --sky: #27a9e1;
    --navy: #123f6e;
    --brand-ink: #2a2361;
    --ink: #3a3a3a;
    --grey: #666666;
    --paper: #ffffff;
    --edge: #9a9a9a;
  }
  * { box-sizing: border-box; margin: 0; padding: 0; }
  html, body {
    width: 971px;
    height: 1200px;
    overflow: hidden;
    background: var(--paper);
    font-family: "Titillium Web", sans-serif;
  }
  .canvas {
    position: relative;
    width: 971px;
    height: 1200px;
  }
  .card {
    position: absolute;
    left: 11px;
    width: 949px;
    text-align: center;
  }
  .card--front {
    top: 11px;
    height: 582px;
    background: var(--sky);
  }
  .card--back {
    top: 604px;
    height: 586px;
    background: var(--paper);
    border: 2px solid var(--edge);
  }
  .wordmark {
    position: absolute;
    left: 0;
    right: 0;
    font-weight: 700;
    letter-spacing: 4px;
    line-height: 1;
  }
  .card--front .wordmark {
    top: 132px;
    font-size: 172px;
    color: var(--paper);
  }
  .card--back .wordmark {
    top: 58px;
    font-size: 158px;
    color: var(--brand-ink);
  }
  .service-band {
    position: absolute;
    background: var(--navy);
    color: var(--paper);
    font-weight: 600;
    display: flex;
    align-items: center;
    justify-content: center;
    letter-spacing: 0.3px;
  }
  .card--front .service-band {
    left: 110px;
    width: 746px;
    top: 348px;
    height: 42px;
    font-size: 28px;
  }
  .card--back .service-band {
    left: 133px;
    width: 666px;
    top: 241px;
    height: 38px;
    font-size: 26px;
  }
  .tagline {
    position: absolute;
    left: 0;
    right: 0;
    top: 412px;
    font-family: "Courgette", cursive;
    font-size: 42px;
    color: var(--paper);
  }
  .contact-line {
    position: absolute;
    left: 0;
    right: 0;
    top: 310px;
    font-size: 42px;
    font-weight: 700;
    color: var(--ink);
    letter-spacing: 0.5px;
    display: flex;
    align-items: center;
    justify-content: center;
  }
  .contact-line .separator {
    display: inline-block;
    width: 11px;
    height: 11px;
    border-radius: 50%;
    background: var(--sky);
    margin: 0 30px;
  }
  .web-detail {
    position: absolute;
    left: 0;
    right: 0;
    font-size: 41px;
    color: var(--grey);
    font-weight: 400;
  }
  .web-detail strong {
    color: var(--sky);
    font-weight: 700;
  }
  .web-detail--email { top: 404px; }
  .web-detail--site { top: 474px; }
</style>
</head>
<body>
<main class="canvas">
  <section class="card card--front" aria-label="Card front">
    <div class="wordmark">TRULOCK</div>
    <div class="service-band">PROPERTY INSPECTIONS &amp; MAINTENANCE</div>
    <p class="tagline">Sound Home, Calm Mind</p>
  </section>

  <section class="card card--back" aria-label="Card back">
    <div class="wordmark">TRULOCK</div>
    <div class="service-band">PROPERTY INSPECTIONS &amp; MAINTENANCE</div>
    <p class="contact-line"><span>OMAR TANVELLI</span><span class="separator" aria-hidden="true"></span><span>0417 828 691</span></p>
    <p class="web-detail web-detail--email"><strong>info</strong>@trulockinspections.com.au</p>
    <p class="web-detail web-detail--site"><strong>www</strong>.trulockinspections.com.au</p>
  </section>
</main>
</body>
</html>
```